QZN Supplements needs a label designer for supplement company

Looking for an on going label designer for my supplement company. I have three products that will need designs. I'm about to launch my sleep supplement called Velmora Rest and that's the first design needed.
I would like all designs to be somewhat simple, not overstated and uniformed so that when you look at all of the labels of the different supplements they are similar and you can tell it's the same brand.
Please see attached sample pictures below as ideas.
Updates

The brand is QZN supplements, logo file has been provided. The supplement is called Velmora Rest. It is a liquid supplement that is a 32/33 ounce white bottle. Die lines and measurements will be provided. Here's text for wording ideas: Wording: Natural Sleep Aid Reset your circadian rhythm. May help you: Fall asleep faster. Get a deeper more restful sleep. Boost Immune System Remember your dreams. Protect your brain and flush toxins. Wake up feeling refreshed. Non-gmo Gluten Free Sugar Free Vegan Manufactured in cGMP factory Manufactured in USA

Target Market(s)

Health and wellness/supplement industry for regular people not hardcore gym goers. My supplements are for a health lifestyle not bodybuilding.

Industry/Entity Type

Health And Wellness

Colors
3176b5
3276b5
33a6d7
85cae6
85abd2
cedeed
e4daeb
b7a5cd

Requirements
Must have
• There will be some text and wording that I will provide that must be on the bottles.

```html
<!DOCTYPE html>
<html lang="en">
<head>
<meta charset="utf-8">
<title>QZN Supplements – Velmora Rest Labels</title>
<link rel="stylesheet" href="https://fonts.googleapis.com/css2?family=Barlow+Condensed:ital,wght@0,700;1,700;1,800&family=Montserrat:wght@300;400&display=swap">
<style>
  :root {
    --canvas: #e6e6e6;
    --white: #ffffff;
    --ink: #111111;
    --blue-deep: #00448a;
    --blue-mid: #3176b5;
    --blue-light: #85abd2;
    --purple-deep: #5e4c84;
    --purple-mid: #b7a5cd;
    --purple-light: #e4daeb;
    --brain-dark: #0b2f6e;
    --brain-glow: #33a6d7;
  }
  * { box-sizing: border-box; margin: 0; padding: 0; }
  html, body {
    width: 1200px;
    height: 1141px;
    overflow: hidden;
    background: var(--canvas);
  }
  .canvas {
    position: relative;
    width: 1200px;
    height: 1141px;
    display: flex;
    justify-content: center;
    align-items: center;
    gap: 80px;
  }
  .label {
    position: relative;
    width: 480px;
    height: 980px;
    border-radius: 18px;
    overflow: hidden;
    box-shadow: 0 10px 30px rgba(0,0,0,0.15);
  }
  .label__header {
    height: 170px;
    background: var(--white);
    display: flex;
    align-items: center;
    justify-content: center;
    gap: 14px;
  }
  .brand__dot {
    width: 54px;
    height: 54px;
    border-radius: 50%;
    border: 3px solid var(--ink);
  }
  .brand__name {
    font-family: "Barlow Condensed", sans-serif;
    font-weight: 700;
    font-size: 46px;
    color: var(--ink);
    text-transform: uppercase;
    letter-spacing: 0.5px;
  }
  .label__body {
    position: relative;
    height: 810px;
    color: var(--white);
  }
  .label--blue .label__body {
    background: linear-gradient(90deg, var(--blue-deep) 0%, var(--blue-mid) 25%, var(--blue-light) 50%, var(--blue-mid) 75%, var(--blue-deep) 100%);
  }
  .label--purple .label__body {
    background: linear-gradient(90deg, var(--purple-deep) 0%, var(--purple-mid) 25%, var(--purple-light) 50%, var(--purple-mid) 75%, var(--purple-deep) 100%);
  }
  .product-name {
    position: absolute;
    top: 60px;
    left: 0;
    right: 0;
    text-align: center;
    font-family: "Barlow Condensed", sans-serif;
    font-style: italic;
    font-weight: 800;
    text-transform: uppercase;
    line-height: 0.85;
  }
  .product-name__first { display: block; font-size: 104px; }
  .product-name__second { display: block; font-size: 150px; }
  .product-tagline {
    position: absolute;
    top: 332px;
    left: 0;
    right: 0;
    text-align: center;
    font-family: "Montserrat", sans-serif;
    font-weight: 300;
    font-size: 29px;
    text-transform: uppercase;
  }
  .benefits {
    position: absolute;
    top: 500px;
    left: 40px;
    list-style: none;
    font-family: "Montserrat", sans-serif;
    font-weight: 300;
    font-size: 28px;
    line-height: 1.3;
  }
  .illustration {
    position: absolute;
    top: 420px;
    right: 18px;
    width: 220px;
    height: 300px;
    border-radius: 46% 46% 40% 40%;
    background: radial-gradient(circle at 50% 55%, var(--brain-glow) 0%, var(--blue-mid) 40%, var(--brain-dark) 100%);
  }
  .net-weight {
    position: absolute;
    bottom: 40px;
    left: 48px;
    font-family: "Barlow Condensed", sans-serif;
    font-weight: 700;
    font-size: 26px;
  }
</style>
</head>
<body>
<main class="canvas">

  <section class="label label--blue">
    <header class="label__header">
      <span class="brand__dot"></span>
      <span class="brand__name">QZN Supplements</span>
    </header>
    <div class="label__body">
      <h1 class="product-name">
        <span class="product-name__first">Velmora</span>
        <span class="product-name__second">Rest</span>
      </h1>
      <p class="product-tagline">Natural Sleep Aid</p>
      <ul class="benefits">
        <li>Fall Asleep<br>Faster</li>
        <li>Stay Asleep<br>Longer</li>
      </ul>
      <div class="illustration" role="img" aria-label="Glowing blue brain illustration with sleeping Z letters"></div>
      <p class="net-weight">Net Wt. 2 LBs (32oz)</p>
    </div>
  </section>

  <section class="label label--purple">
    <header class="label__header">
      <span class="brand__dot"></span>
      <span class="brand__name">QZN Supplements</span>
    </header>
    <div class="label__body">
      <h1 class="product-name">
        <span class="product-name__first">Velmora</span>
        <span class="product-name__second">Rest</span>
      </h1>
      <p class="product-tagline">Natural Sleep Aid</p>
      <ul class="benefits">
        <li>Fall Asleep<br>Faster</li>
        <li>Stay Asleep<br>Longer</li>
      </ul>
      <div class="illustration" role="img" aria-label="Glowing blue brain illustration with sleeping Z letters"></div>
      <p class="net-weight">Net Wt. 2 LBs (32oz)</p>
    </div>
  </section>

</main>
</body>
</html>
```